FOLI PACK FOR STICKS

Design the packaging for salted sticks (weight 400g) reference to the logo TOVEN (in attached).
Color packaging- look forward to suggestions.
Package with window.
Hi, we need only graphic conception without texts on back side.

Please find Logo TOVEN and the grid of packaging - attached
Updates

we need only graphic conception without texts on back side. Added Saturday, November 08, 2014

Target Market(s)

typical salted snack for everyone (adults and children included)

Font styles to use
Sans Serif

Requirements
Should not have
• - religion and politic signs…
• - toys and childdraws
• - monsters, devils and demons etc.

```html
<!DOCTYPE html>
<html lang="en">
<head>
<meta charset="utf-8">
<title>TOVEN Pretzel Sticks – 400g pack front</title>
<link rel="stylesheet" href="https://fonts.googleapis.com/css2?family=Lilita+One&family=Roboto+Condensed:wght@700&display=swap">
<style>
  :root {
    --stage: #1e1e1e;
    --pack-red: #d3161c;
    --pack-red-deep: #8f0a0f;
    --pack-red-light: #f04a3a;
    --crimp-red: #b01015;
    --title-orange: #f7931e;
    --title-orange-deep: #e0600a;
    --title-outline: #ffffff;
    --brand-cream: #fbe9c4;
    --band-gold: #f9c21a;
    --band-gold-deep: #e79a0c;
    --sticks-light: #f3c06a;
    --sticks-deep: #c57a25;
    --navy: #1b2d63;
    --navy-deep: #101c42;
    --label-white: #ffffff;
  }
  html, body {
    margin: 0;
    padding: 0;
    width: 1200px;
    height: 920px;
    overflow: hidden;
    background: var(--stage);
  }
  .canvas {
    display: block;
    width: 1200px;
    height: 920px;
  }
  .brand-name {
    font-family: "Lilita One", "Arial Black", sans-serif;
    font-size: 44px;
    fill: var(--brand-cream);
    letter-spacing: 2px;
  }
  .product-title {
    font-family: "Lilita One", "Arial Black", sans-serif;
    font-size: 128px;
    fill: url(#titleFill);
    stroke: var(--title-outline);
    stroke-width: 10px;
    paint-order: stroke fill;
    stroke-linejoin: round;
  }
  .net-weight {
    font-family: "Roboto Condensed", "Arial Narrow", sans-serif;
    font-weight: 700;
    font-size: 40px;
    fill: var(--label-white);
  }
</style>
</head>
<body>
<svg class="canvas" viewBox="0 0 1200 920" xmlns="http://www.w3.org/2000/svg">
  <defs>
    <radialGradient id="redGlow" cx="0.5" cy="0.38" r="0.7">
      <stop offset="0" stop-color="var(--pack-red-light)"/>
      <stop offset="0.55" stop-color="var(--pack-red)"/>
      <stop offset="1" stop-color="var(--pack-red-deep)"/>
    </radialGradient>
    <linearGradient id="titleFill" x1="0" y1="0" x2="0" y2="1">
      <stop offset="0" stop-color="#ffc04a"/>
      <stop offset="0.5" stop-color="var(--title-orange)"/>
      <stop offset="1" stop-color="var(--title-orange-deep)"/>
    </linearGradient>
    <linearGradient id="sticksFill" x1="0" y1="0" x2="1" y2="0">
      <stop offset="0" stop-color="var(--sticks-deep)"/>
      <stop offset="0.5" stop-color="var(--sticks-light)"/>
      <stop offset="1" stop-color="var(--sticks-deep)"/>
    </linearGradient>
    <linearGradient id="goldBand" x1="0" y1="0" x2="0" y2="1">
      <stop offset="0" stop-color="var(--band-gold)"/>
      <stop offset="1" stop-color="var(--band-gold-deep)"/>
    </linearGradient>
    <linearGradient id="navyFill" x1="0" y1="0" x2="0" y2="1">
      <stop offset="0" stop-color="var(--navy)"/>
      <stop offset="1" stop-color="var(--navy-deep)"/>
    </linearGradient>
    <radialGradient id="shakerTone" cx="0.5" cy="0.5" r="0.5">
      <stop offset="0" stop-color="#e9eef8"/>
      <stop offset="1" stop-color="#9fb0d6" stop-opacity="0.3"/>
    </radialGradient>
    <clipPath id="packShape">
      <rect x="330" y="40" width="540" height="840" rx="10"/>
    </clipPath>
  </defs>

  <g class="pack" clip-path="url(#packShape)">
    <!-- red upper body -->
    <rect class="pack-body" x="330" y="40" width="540" height="840" fill="url(#redGlow)"/>

    <!-- top crimp -->
    <rect class="crimp-top" x="330" y="40" width="540" height="34" fill="var(--crimp-red)"/>
    <g class="crimp-lines" stroke="#7a080c" stroke-width="1.5" opacity="0.5">
      <line x1="330" y1="48" x2="870" y2="48"/>
      <line x1="330" y1="56" x2="870" y2="56"/>
      <line x1="330" y1="64" x2="870" y2="64"/>
    </g>

    <!-- brand -->
    <g class="brand">
      <circle cx="600" cy="118" r="14" fill="var(--brand-cream)"/>
      <text class="brand-name" x="600" y="182" text-anchor="middle">TOVEN</text>
    </g>

    <!-- product title -->
    <g class="title">
      <text class="product-title" x="600" y="330" text-anchor="middle">Pretzel</text>
      <text class="product-title" x="600" y="448" text-anchor="middle">Sticks</text>
    </g>

    <!-- window with sticks -->
    <path class="sticks-window" role="img" aria-label="Window showing golden salted pretzel sticks"
          d="M330 540 C 470 505, 640 520, 870 490 L 870 720 C 700 720, 500 750, 330 745 Z"
          fill="url(#sticksFill)"/>

    <!-- gold border above window -->
    <path class="gold-rim" d="M330 530 C 470 495, 640 510, 870 480 L 870 494 C 640 524, 470 509, 330 544 Z"
          fill="url(#goldBand)"/>

    <!-- navy base with gold wave -->
    <path class="gold-wave" d="M330 720 C 500 745, 700 690, 870 660 L 870 880 L 330 880 Z" fill="url(#goldBand)"/>
    <path class="navy-base" d="M330 736 C 500 762, 700 706, 870 676 L 870 880 L 330 880 Z" fill="url(#navyFill)"/>

    <!-- salt shaker area -->
    <ellipse class="salt-shaker" role="img" aria-label="Salt shaker sprinkling salt"
             cx="770" cy="760" rx="80" ry="60" fill="url(#shakerTone)" opacity="0.55"/>

    <text class="net-weight" x="372" y="822">400g</text>

    <!-- bottom crimp -->
    <rect class="crimp-bottom" x="330" y="846" width="540" height="34" fill="var(--navy-deep)"/>
    <g class="crimp-lines" stroke="#0a1230" stroke-width="1.5" opacity="0.6">
      <line x1="330" y1="856" x2="870" y2="856"/>
      <line x1="330" y1="864" x2="870" y2="864"/>
      <line x1="330" y1="872" x2="870" y2="872"/>
    </g>
  </g>
</svg>
</body>
</html>
```